Infografik für Tanzschule
Zielgruppe
Wir sind eine Tanzschule für die Tänze Salsa, Bachata, kizomba & Zouk in Freiburg
Aufgabenstellung
DESIGN-BRIEFING
Tarifübersicht – Tanzschule Ritmo del Alma
Projektziel
Gestaltung einer klaren, hochwertigen Tarifübersicht für eine Tanzschule.
Die Grafik dient: als Information & Orientierung auf der Homepage, als visuelle Grundlage für das Anmeldeformular vor Ort, Der Einstieg erfolgt immer über eine gratis Schnupperstunde.
Die verbindliche Anmeldung erfolgt nach der Schnupperstunde vor Ort über ein Formular mit Auswahlkästchen.
Grundaufbau
3 Tarifkarten nebeneinander
Einheitlicher, moderner Stil
evtl. Emotionale Bilder (echte Tanzszenen, echte Menschen)
Klare Hierarchie:
Titel → Preis → Erklärung → Vorteile → Auswahlkästchen
Struktur der Tarifkarten
KARTE 1 – EINSTIEG
Titel: 1× PRO WOCHE TANZEN
Preis: 56 €/ 39 € erm.
Subline: pro Person · pro Kalendermonat
Vorteile (max. 4 Bulletpoints):
Ein fester wöchentlicher Kurs
Klare Routine & Struktur
Ausweichstunde im selben Monat möglich (muss klar enthalten sein)
Auswahl: ☐ 1× pro Woche tanzen
KARTE 2 – REGELMÄSSIG TANZEN (darf visuell leicht hervorgehoben sein, z. B. Rahmen oder Badge)
Optionales Badge:
SEHR BELIEBT
Titel: 2× PRO WOCHE TANZEN
Preis: 98 € / 68 € erm.
Vorteile:
Zwei feste wöchentliche Kurse
Mehr Praxis & schnellerer Fortschritt
Ausweichstunde im selben Monat möglich
Auswahl:
☐ 2× pro Woche tanzen
KARTE 3 – MAXIMALE FREIHEIT
Titel: FLAT – ALL YOU CAN DANCE
Preis: ab 129 € / 99 € erm.
Alle Tänze
Alle Kurse (für dein Tanz-Level)
Alle Workshops (für dein Tanz-Level)
Maximale Freiheit
☐ FLAT 1 Monat – 149 € | 119 € erm. (monatlich kündbar)
☐ FLAT 3 Monate – 129 € | 99 € erm. (3 Monate Erstlaufzeit)
Einheitlicher Hinweis unter den Karten (kleiner Text)
Ausweic..

```html
<!DOCTYPE html>
<html lang="de">
<head>
<meta charset="utf-8">
<title>Tarife</title>
<link rel="stylesheet" href="https://fonts.googleapis.com/css2?family=Barlow+Condensed:wght@700&family=Montserrat:wght@300;400;600;700&family=Open+Sans:wght@400;600&display=swap">
<style>
  :root {
    --green: #5e8b76;
    --crimson: #b01c4e;
    --ink: #231f20;
    --card-bg: #f8f8f8;
    --card-bg-accent: #faf5f7;
    --text: #2a2a2a;
  }
  * { margin: 0; padding: 0; box-sizing: border-box; }
  html, body { width: 1200px; height: 1200px; overflow: hidden; background: #fff; }
  .canvas { position: relative; width: 1200px; height: 1200px; font-family: "Open Sans", sans-serif; color: var(--text); }
  .page-title {
    position: absolute; left: 163px; top: 146px;
    font-family: "Barlow Condensed", sans-serif; font-weight: 700;
    font-size: 48px; letter-spacing: 0.5px; color: var(--crimson); line-height: 1;
  }
  .plan {
    position: absolute; top: 258px; width: 274px; height: 642px;
    background: var(--card-bg); text-align: center;
  }
  .plan--basic { left: 164px; color: var(--green); --accent: var(--green); }
  .plan--regular { left: 464px; color: var(--crimson); --accent: var(--crimson); background: var(--card-bg-accent); }
  .plan--flat { left: 764px; color: var(--ink); --accent: var(--ink); }
  .plan-header { position: absolute; left: 0; top: 0; width: 274px; height: 112px; }
  .plan-header svg { position: absolute; inset: 0; }
  .plan-header svg path { fill: var(--accent); }
  .plan-name {
    position: absolute; left: 0; right: 0; top: 24px; color: #fff;
    font-family: "Montserrat", sans-serif; font-weight: 700; font-size: 15px; letter-spacing: 0.2px;
  }
  .plan-tagline {
    position: absolute; left: 0; right: 0; top: 46px; color: #fff;
    font-family: "Montserrat", sans-serif; font-weight: 400; font-size: 11.5px;
  }
  .plan--regular .plan-name { top: 26px; }
  .plan--regular .plan-tagline { top: 48px; }
  .price {
    position: absolute; left: 0; right: 0; top: 168px;
    font-family: "Montserrat", sans-serif; line-height: 1; white-space: nowrap;
  }
  .price-main { font-size: 42px; font-weight: 300; }
  .plan--regular .price-main, .plan--flat .price-main { font-weight: 600; }
  .price-reduced { font-size: 15.5px; font-weight: 600; margin-left: 4px; }
  .price-note {
    position: absolute; left: 0; right: 0; top: 208px;
    font-family: "Open Sans", sans-serif; font-weight: 400; font-size: 15px; opacity: 0.95;
  }
  .plan--basic .price-note, .plan--regular .price-note { font-weight: 300; }
  .perk, .option {
    position: absolute; left: 12px; right: 12px; font-size: 13.7px; line-height: 19px;
  }
</style>
</head>
<body>
<div class="canvas">
  <h1 class="page-title">TARIFE</h1>

  <section class="plan plan--basic">
    <div class="plan-header">
      <svg width="274" height="112" viewBox="0 0 274 112"><path d="M0 0H274V88C250 96 228 100 200 96C170 92 150 84 120 88C80 93 40 112 0 109Z"/></svg>
      <div class="plan-name">EINSTIEG</div>
      <div class="plan-tagline">DANCE 1 PER WEEK</div>
    </div>
    <div class="price"><span class="price-main">56 €</span><span class="price-reduced">/ 39 € erm</span></div>
    <div class="price-note">pro Person · pro Kalendermonat</div>
    <p class="perk" style="top:289px">Ein fester wöchentlicher Kurs</p>
    <p class="perk" style="top:321px">Klare Routine &amp; Struktur</p>
    <p class="perk" style="top:372px">Ausweichstunde im selben Monat<br>möglich</p>
    <p class="option" style="top:483px">* 1× pro Woche tanzen</p>
  </section>

  <section class="plan plan--regular">
    <div class="plan-header">
      <svg width="274" height="112" viewBox="0 0 274 112"><path d="M0 0H274V88C250 96 228 100 200 96C170 92 150 84 120 88C80 93 40 112 0 109Z"/></svg>
      <div class="plan-name">REGELMÄSSIG TANZEN</div>
      <div class="plan-tagline">DANCE 2 PER WEEK</div>
    </div>
    <div class="price"><span class="price-main">98 €</span><span class="price-reduced">/ 68 € erm</span></div>
    <div class="price-note">pro Person · pro Kalendermonat</div>
    <p class="perk" style="top:289px">Zwei feste wöchentliche Kurse</p>
    <p class="perk" style="top:321px">Mehr Praxis &amp; schnellerer<br>Fortschritt</p>
    <p class="perk" style="top:372px">Ausweichstunde im selben Monat<br>möglich</p>
    <p class="option" style="top:483px">* 2× pro Woche tanzen</p>
  </section>

  <section class="plan plan--flat">
    <div class="plan-header">
      <svg width="274" height="112" viewBox="0 0 274 112"><path d="M0 0H274V88C250 96 228 100 200 96C170 92 150 84 120 88C80 93 40 112 0 109Z"/></svg>
      <div class="plan-name">MAXIMALE FREIHEIT</div>
      <div class="plan-tagline">FLAT – ALL YOU CAN DANCE</div>
    </div>
    <div class="price"><span class="price-main">129 €</span><span class="price-reduced">/ 99 € erm</span></div>
    <div class="price-note">pro Person · pro Kalendermonat</div>
    <p class="perk" style="top:289px">Alle Tänze</p>
    <p class="perk" style="top:321px">Alle Kurse (für dein Tanz-Level)</p>
    <p class="perk" style="top:372px">Alle Workshops (für dein Tanz-Level)</p>
    <p class="perk" style="top:422px">Maximale Freiheit</p>
    <p class="option" style="top:483px;left:4px;right:4px">* FLAT 1 Monat – 149 € | 119 € erm.<br>(monatlich kündbar)</p>
    <p class="option" style="top:534px;left:4px;right:4px">* FLAT 3 Monate – 129 € | 99 € erm.<br>(3 Monate Erstlaufzeit)</p>
  </section>

  <footer>
    <p style="position:absolute;left:189px;top:997px;font-size:13px;font-weight:600;color:var(--text)">Ausweichstunde: Im selben Kalendermonat möglich.</p>
    <p style="position:absolute;left:189px;top:1035px;width:820px;font-size:13px;line-height:19px;color:var(--text)">Verlängerung &amp; Kündigung: Der Vertrag verlängert sich automatisch um jeweils einen Monat und ist mit 14 Tagen Frist zum Monatsende kündbar. Ausnahme: FLAT 3 Monate – kündbar nach Ablauf der Erstlaufzeit.</p>
  </footer>
</div>
</body>
</html>
```